Electrical Wholesaler Needs a New Website

Looking for a new website to be built for an electrical wholesaler based in Birmingham(England). Our logo is based on two Lions with a shield, so ideally the site should be deigned around that.

Looking for something that shows off our logo and incorporates what we are trying to do, preferably to have a colour scheme that is green and black if possible.

Reason: Still undecided on what I'm looking for

Reason: Need more time to decide

Target Market(s)

I'm looking for a professional website for my company that doesn't just look like amother WordPress template that I could build myself.

Industry/Entity Type

Electrical

Font styles to use
Sans Serif

Colors
9bcb3c
cadf82

Requirements
Must have
• Website with 4-5 pages, home page, about us, suppliers list, catalogue download and contact us. Search for UK electrical wholesalers to give you an idea of what I mean.

```html
<!DOCTYPE html>
<html lang="en">
<head>
<meta charset="utf-8">
<title>Brightwire Electrical Wholesalers</title>
<link rel="stylesheet" href="https://fonts.googleapis.com/css2?family=PT+Sans:wght@400;700&display=swap">
<style>
:root{
  --green:#9bcb3c;
  --green-dark:#6fa31f;
  --green-light:#cadf82;
  --black:#222;
  --topbar:#2b2b2b;
  --text:#333;
  --grey:#bdbdbd;
  --page:#f4f4f4;
}
*{margin:0;padding:0;box-sizing:border-box}
html,body{width:900px;height:1200px;overflow:hidden}
body{background:var(--page);font-family:"PT Sans",sans-serif;color:var(--text);position:relative}
.abs{position:absolute}
.topbar{left:0;top:0;width:900px;height:24px;background:var(--topbar)}
.client-login{left:706px;top:4px;font-size:11px;color:var(--green);display:flex;align-items:center;gap:6px}
.client-login .dot{width:13px;height:13px;border-radius:50%;background:#777}
.header{left:0;top:24px;width:900px;height:126px;background:#fafafa}
.brand{left:100px;top:70px;display:flex;align-items:center;gap:8px}
.brand .mark{width:22px;height:22px;background:var(--green-dark)}
.brand .name{font-size:22px;font-weight:700;color:var(--green-dark);line-height:1}
.brand-sub{left:100px;top:97px;font-size:9px;font-weight:700;color:var(--green-dark);letter-spacing:.5px}
.phone{left:662px;top:42px;display:flex;align-items:center;gap:10px;font-size:17px;color:#333}
.icon-box{width:16px;height:16px;background:var(--green);display:flex;align-items:center;justify-content:center}
.email{left:662px;top:73px;display:flex;align-items:center;gap:10px;font-size:10px;color:#333}
.search{left:566px;top:110px;display:flex}
.search input{width:178px;height:17px;border:1px solid #ccc;font:10px "PT Sans",sans-serif;padding-left:5px;color:#999;background:#fff}
.search .btn{width:47px;height:17px;background:var(--green);color:#fff;font-size:9px;display:flex;align-items:center;justify-content:center}
.nav{left:0;top:150px;width:900px;height:34px;background:linear-gradient(#a6d44a,#86bb2a);border-bottom:1px solid #6e9e20}
.nav a{position:absolute;top:0;height:34px;line-height:34px;color:#fff;font-size:12.5px;text-decoration:none;padding:0 0}
.nav .sep{position:absolute;top:4px;width:1px;height:26px;background:rgba(0,0,0,.12)}
.nav a.active{background:#fff;color:#222;width:73px;text-align:center;left:101px;height:35px}
.slider-band{left:0;top:184px;width:900px;height:288px;background:linear-gradient(#f6f6f6,#dedede)}
.slider{left:84px;top:198px;width:730px;height:274px;background:var(--grey);padding:5px}
.slide-img{width:720px;height:264px;background:radial-gradient(circle at 45% 40%,#c0d7b6,#e9e9e9 40%,#f3f3f3 60%,#d9d9d9);}
.caption{left:578px;top:345px;width:230px;height:65px;background:rgba(70,70,70,.85);color:#fff;padding:12px 10px;font-variant:small-caps;font-size:17px;line-height:23px}
.caption b{color:var(--green);font-weight:400}
.dots{left:721px;top:440px;display:flex;gap:4px}
.dots span{width:18px;height:18px;border-radius:50%;background:#234;color:#fff;font-size:11px;display:flex;align-items:center;justify-content:center;background:#1a3a1a}
.dots span.on{background:var(--green)}
.side{left:88px;top:494px;width:173px;height:303px;background:#fff;border:1px solid #ddd}
.side-title{left:86px;top:498px;width:115px;height:24px;background:var(--green);color:#fff;font-size:14px;padding-left:17px;line-height:24px;clip-path:polygon(0 0,94% 0,100% 100%,0 100%)}
.side ul{list-style:none;position:absolute;top:32px;left:0;width:171px}
.side li{height:27px;line-height:27px;font-size:11px;color:#222;padding-left:24px;position:relative;background:linear-gradient(#b6dc6a,#9bcb3c);border-bottom:1px solid #fff}
.side li::before{content:"";position:absolute;left:10px;top:10px;width:7px;height:7px;background:#4d6e16}
.side li.active{background:var(--green-dark);color:#fff}
.side li.active::before{background:#fff}
.side li.sub{background:#fff;padding-left:31px;font-size:10px}
.side li.sub::before{content:"›";background:none;left:22px;top:0;width:auto;height:auto;color:#444}
.promo{left:87px;top:813px;width:175px;height:209px;background:var(--green);border:2px solid #7fb22a;border-radius:3px}
.promo-img{position:absolute;left:2px;top:2px;width:167px;height:103px;background:linear-gradient(#bcc7d0,#8da2b4)}
.promo h3{position:absolute;left:6px;top:111px;font-size:15px;font-weight:400;font-variant:small-caps;color:#fff}
.promo p{position:absolute;left:5px;top:132px;font-size:11px;line-height:17px;color:#fff}
.promo .cta{position:absolute;left:28px;top:170px;width:120px;height:26px;background:#111;border-radius:3px;color:#fff;font-variant:small-caps;font-size:13px;display:flex;align-items:center;justify-content:center}
.h2{font-size:19px;font-variant:small-caps;color:#333;font-weight:400}
.h2 b{color:var(--green-dark);font-weight:400}
.welcome{left:286px;top:490px}
.rule{height:1px;background:#e2e2e2;width:522px;left:286px}
.body-text{left:287px;width:521px;font-size:9.6px;line-height:16px;text-align:justify;color:#222}
.learn{left:732px;top:669px;width:70px;height:24px;background:var(--green);color:#fff;font-size:8px;display:flex;align-items:center;justify-content:center}
.arrows{left:756px;top:733px;display:flex;gap:3px}
.arrows span{width:19px;height:19px;background:#222;border-radius:3px;color:#fff;font-size:9px;display:flex;align-items:center;justify-content:center}
.card{width:153px;height:106px;box-shadow:2px 2px 3px rgba(0,0,0,.35)}
.card .label{position:absolute;left:0;bottom:0;width:100%;height:28px;background:rgba(60,60,60,.8);color:#fff;font-variant:small-caps;font-size:15px;line-height:28px;padding-left:7px}
.footer{left:0;top:1073px;width:900px;height:127px;background:radial-gradient(circle at 30% 40%,#a6cb63,#6e9c34 70%)}
.footer h4{position:absolute;left:90px;top:20px;color:#fff;font-size:14px;font-weight:400}
.footer input{position:absolute;left:90px;top:48px;width:194px;height:23px;border:1px solid #ccc;font:italic 8px "PT Sans",sans-serif;padding-left:13px;color:#888}
.footer .sub{position:absolute;left:206px;top:80px;width:78px;height:24px;background:var(--green);color:#fff;font-variant:small-caps;font-size:13px;display:flex;align-items:center;justify-content:center}
.social{position:absolute;left:632px;top:16px;display:flex;gap:10px}
.social span{width:19px;height:19px;background:#3f5f9a;border:1px solid #fff}
.legal{position:absolute;right:106px;top:45px;color:#fff;font-size:9.6px;text-align:right;line-height:18px}
</style>
</head>
<body>
<div class="abs topbar"></div>
<div class="abs client-login"><span class="dot"></span>Client Login</div>

<div class="abs header"></div>
<div class="abs brand"><span class="mark"></span><span class="name">BRIGHTWIRE</span></div>
<div class="abs brand-sub">ELECTRICAL WHOLESALERS</div>
<div class="abs phone">
  <span class="icon-box"><svg width="10" height="10" viewBox="0 0 10 10"><path d="M2 1l2 2-1 1c.5 1.2 1.8 2.5 3 3l1-1 2 2-1.5 1.5C4 9 1 6 .5 2.5z" fill="#333"/></svg></span>0121 000 4827
</div>
<div class="abs email">
  <svg width="16" height="10" viewBox="0 0 16 10"><rect x="0.5" y="0.5" width="15" height="9" fill="none" stroke="#333"/><path d="M.5.5L8 6l7.5-5.5" fill="none" stroke="#333"/></svg>sales@brightwire-elec.co.uk
</div>
<div class="abs search"><input value="type your word here" aria-label="Search"><span class="btn">SEARCH</span></div>

<nav class="abs nav">
  <a class="active" href="#">Home</a>
  <a href="#" style="left:193px">About Us</a><span class="sep" style="left:258px"></span>
  <a href="#" style="left:280px">Services</a><span class="sep" style="left:339px"></span>
  <a href="#" style="left:360px">Products</a><span class="sep" style="left:421px"></span>
  <a href="#" style="left:445px">Pricing</a><span class="sep" style="left:501px"></span>
  <a href="#" style="left:521px">News</a><span class="sep" style="left:569px"></span>
  <a href="#" style="left:591px">Testimonials</a><span class="sep" style="left:675px"></span>
  <a href="#" style="left:695px">Contact Us</a>
</nav>

<div class="abs slider-band"></div>
<div class="abs slider"><div class="slide-img" role="img" aria-label="Photo of coiled cables, wiring harnesses and electrical connectors"></div></div>
<div class="abs caption">We are an <b>Electrical Products</b><br>wholesale company.</div>
<div class="abs dots"><span>1</span><span class="on">2</span><span>3</span><span>4</span></div>

<aside class="abs side">
  <ul>
    <li class="active">Cable</li>
    <li class="sub">Special Selection</li>
    <li>Cable Management</li>
    <li>Heating &amp; Ventillation</li>
    <li>Distribution, Switchgear</li>
    <li>Lamps</li>
    <li>Lighting</li>
    <li>Security, Safety &amp; Emergency</li>
    <li>Tools, Test &amp; Site Equipment</li>
    <li>Wiring Accessories</li>
  </ul>
</aside>
<div class="abs side-title">Products</div>

<div class="abs promo">
  <div class="promo-img" role="img" aria-label="Photo of two wall-mounted fan heaters"></div>
  <h3>Ventara</h3>
  <p>Compact Commercial Fan Heaters<br>The VFH Range</p>
  <div class="cta">Click Here</div>
</div>

<h2 class="abs h2 welcome">Welcome To <b>Brightwire</b></h2>
<div class="abs rule" style="top:518px"></div>
<p class="abs body-text" style="top:528px">Sed ut perspiciatis unde omnis iste natus error sit voluptatem accusantium doloremque laudantium, totam rem aperiam, eaque ipsa quae ab illo inventore veritatis et quasi architecto beatae vitae dicta sunt explicabo. Nemo enim ipsam voluptatem quia voluptas sit aspernatur aut odit aut fugit, sed quia consequuntur magni dolores eos qui ratione voluptatem sequi nesciunt.</p>
<p class="abs body-text" style="top:592px">Sed ut perspiciatis unde omnis iste natus error sit voluptatem accusantium doloremque laudantium, totam rem aperiam, eaque ipsa quae ab illo inventore veritatis et quasi architecto beatae vitae dicta sunt explicabo. Nemo enim ipsam voluptatem quia voluptas sit aspernatur aut odit aut fugit, sed quia consequuntur magni dolores eos qui ratione voluptatem sequi nesciunt. Neque porro quisquam est, qui dolorem ipsum quia dolor sit amet.Sed ut perspiciatis unde omnis iste natus error sit voluptatem accusantium doloremque.</p>
<div class="abs learn">LEARN MORE</div>

<h2 class="abs h2" style="left:286px;top:731px">Our <b>Products</b></h2>
<div class="abs rule" style="top:759px"></div>
<div class="abs arrows"><span>»</span><span>«</span></div>

<div class="abs card" style="left:296px;top:769px;background:linear-gradient(#8ed68c,#6b8f5e)" role="img" aria-label="Photo of stripped copper cable"><div class="label">Cable</div></div>
<div class="abs card" style="left:469px;top:769px;background:linear-gradient(#f6dfa4,#7d8288)" role="img" aria-label="Photo of a cable management tray"><div class="label">Cable Management</div></div>
<div class="abs card" style="left:642px;top:769px;background:linear-gradient(#6c7476,#9aa39c)" role="img" aria-label="Photo of a wall-mounted patio heater"><div class="label">Heating &amp; Ventilation</div></div>
<div class="abs card" style="left:296px;top:912px;background:linear-gradient(#f09a88,#e8e8e8)" role="img" aria-label="Photo of a white switchgear unit with red switch"><div class="label">Switchgear</div></div>
<div class="abs card" style="left:469px;top:912px;background:linear-gradient(#c9cfcf,#8e9696)" role="img" aria-label="Photo of halogen light bulbs"><div class="label">Lamps</div></div>
<div class="abs card" style="left:642px;top:912px;background:linear-gradient(#b8d86e,#a6acb2)" role="img" aria-label="Photo of twin emergency floodlights"><div class="label">Lighting</div></div>

<footer class="abs footer">
  <h4>Newsletter</h4>
  <input value="Your Email Id" aria-label="Your email">
  <div class="sub">Subscribe</div>
  <div class="social"><span></span><span style="background:#3fb0e0"></span><span style="background:#333"></span><span style="background:#e8902a"></span><span style="background:#c8221e"></span><span style="background:#7a98c0"></span></div>
  <div class="legal">Terms of Use - Privacy Statement - Disclaimer<br>© 2013 &nbsp;brightwire, All Rights Reserved</div>
</footer>
</body>
</html>
```